Staffing and Consulting Service Company needs Business Cards

We need to have business cards for our business. You can check our website www.talvrenix.com to see the branding we are using. The logo is in the website.
We use a tag line Staffing & Consulting Solutions Made Easy.
We use different blues in the logo and we use the red for the Company name.
As you can see in the website there is a gradient in the bottom part of each page that includes some of the dots we use for the logo.
We will need the following fields on the design:
Company Name
Employee Name
Title
Address
Tel
Email
Website
Can be Single or Double Sided
There is no preference for single or double sided.
Target Market(s)
Companies in need of IT staffing and IT consulting services
Industry/Entity Type
Business
Look and feel

```html
<!DOCTYPE html>
<html lang="en">
<head>
<meta charset="utf-8">
<title>Talvrenix Business Card</title>
<link rel="stylesheet" href="https://fonts.googleapis.com/css2?family=Arimo:wght@700&family=Open+Sans:ital,wght@0,400;0,600;1,400&display=swap">
<style>
  :root {
    --page-bg: #d9dce1;
    --card-white: #ffffff;
    --header-fade: #eef1f5;
    --body-light: #dfe4eb;
    --body-mid: #7e93ad;
    --body-deep: #1d3d63;
    --navy: #1c3666;
    --accent-blue: #1f4f7d;
    --curve-blue: #2a84c6;
    --corner-fill: #e4eff9;
    --tag-blue: #2f6ea8;
    --text-white: #ffffff;
  }
  * { margin: 0; padding: 0; box-sizing: border-box; }
  html, body {
    width: 1200px; height: 1200px; overflow: hidden;
    background: var(--page-bg);
  }
  .canvas {
    position: relative; width: 1200px; height: 1200px;
    display: flex; align-items: center; justify-content: center;
  }
  .business-card {
    position: relative; width: 1050px; height: 600px; overflow: hidden;
    background: var(--card-white);
    box-shadow: 0 10px 30px rgba(0,0,0,0.25);
  }
  .card-body {
    position: absolute; left: 0; right: 0; top: 118px; bottom: 0;
    background: linear-gradient(180deg, var(--body-light) 0%, var(--body-mid) 38%, var(--body-deep) 100%);
  }
  .header-band {
    position: absolute; left: 0; right: 0; top: 0; height: 118px;
    background: linear-gradient(180deg, var(--card-white) 0%, var(--header-fade) 100%);
  }
  .divider {
    position: absolute; left: 0; top: 0; width: 1050px; height: 130px;
  }
  .company-title {
    position: absolute; left: 62px; top: 26px;
    font-family: "Arimo", Arial, sans-serif; font-weight: 700;
    font-size: 28px; line-height: 30px; color: var(--navy);
    text-align: center;
  }
  .tagline {
    position: absolute; left: 96px; top: 92px;
    font-family: "Open Sans", sans-serif; font-size: 15px;
    color: var(--tag-blue); letter-spacing: 0.3px;
  }
  .brand-name {
    position: absolute; right: 50px; top: 28px;
    font-family: "Arimo", Arial, sans-serif; font-weight: 700;
    font-size: 28px; color: var(--navy); letter-spacing: 0.5px;
  }
  .corner-curve {
    position: absolute; left: 0; top: 0; width: 1050px; height: 600px;
  }
  .holder-name {
    position: absolute; left: 54px; top: 285px;
    font-family: "Open Sans", sans-serif; font-weight: 400; font-size: 24px; letter-spacing: 2px;
    color: var(--text-white); padding-bottom: 4px;
    border-bottom: 2px solid var(--text-white); padding-right: 36px;
  }
  .contact-list {
    position: absolute; left: 44px; top: 338px;
    font-family: "Open Sans", sans-serif; font-size: 21px;
    color: var(--text-white);
    display: grid; grid-template-columns: 120px auto; row-gap: 6px;
  }
  .contact-label { font-style: italic; }
  .social-row {
    position: absolute; right: 56px; bottom: 58px;
    display: flex; align-items: center; gap: 6px;
  }
  .social-heading {
    font-family: "Arimo", Arial, sans-serif; font-weight: 700;
    font-size: 21px; color: var(--navy); margin-right: 10px;
  }
  .social-dot { width: 24px; height: 24px; border-radius: 50%; background: var(--accent-blue); }
</style>
</head>
<body>
<main class="canvas">
  <article class="business-card">
    <div class="card-body" role="img" aria-label="Blue gradient background with a soft pattern of brand dots"></div>
    <div class="header-band"></div>

    <svg class="divider" viewBox="0 0 1050 130" aria-hidden="true">
      <line x1="0" y1="118" x2="1050" y2="118" stroke="var(--accent-blue)" stroke-width="3"/>
      <line x1="560" y1="75" x2="742" y2="75" stroke="var(--accent-blue)" stroke-width="2"/>
      <line x1="788" y1="75" x2="1050" y2="75" stroke="var(--accent-blue)" stroke-width="2"/>
      <circle cx="765" cy="75" r="17" fill="var(--accent-blue)"/>
    </svg>

    <svg class="corner-curve" viewBox="0 0 1050 600" aria-hidden="true">
      <path d="M650 600 C 690 470, 800 440, 900 420 C 990 402, 1030 370, 1050 330 L1050 600 Z" fill="var(--corner-fill)"/>
      <path d="M650 600 C 690 470, 800 440, 900 420 C 990 402, 1030 370, 1050 330" fill="none" stroke="var(--curve-blue)" stroke-width="3"/>
    </svg>

    <h1 class="company-title">STAFFING AND CONSULTING<br>SERVICE COMPANY</h1>
    <p class="tagline">Staffing &amp; Consulting Solutions Made Easy.</p>

    <span class="brand-name">Talvrenix</span>

    <h2 class="holder-name">YOUR NAME HERE</h2>
    <dl class="contact-list">
      <dt class="contact-label">Title :</dt><dd>Your Title Here</dd>
      <dt class="contact-label">Address :</dt><dd>Address line 1,Address line 2,City,State,02234</dd>
      <dt class="contact-label">Tel :</dt><dd>(555) 214-7390</dd>
      <dt class="contact-label">Email :</dt><dd>Yourcompany@talvrenix.com</dd>
      <dt class="contact-label">Website :</dt><dd>www.talvrenix.com</dd>
    </dl>

    <div class="social-row">
      <span class="social-heading">FIND US ON</span>
      <span class="social-dot"></span>
      <span class="social-dot"></span>
      <span class="social-dot"></span>
      <span class="social-dot"></span>
    </div>
  </article>
</main>
</body>
</html>
```